Electrical company business card design.

Hi, were an electrical company in Auckland New Zealand called Quarneth Ltd. We focus mainly on high end residential and commercial so the card would be targeted towards that.
The card will be for myself, i am the director of the company.
Name: Derek Olstow
Position: Director/electrician
Phone: 021 387 9415
Email: derek@quarneth.co.nz
Location: Auckland
As for colors the the blue color in the logo is preferred, i also don't mind a black background option.
Target Market(s)
High end residential and commercial
Industry/Entity Type
Electrician
Contact Information for Business Card
Name: Derek Olstow Position: Director/Electrician Phone: 021 387 9415, Email: derek@quarneth.co.nz, Location: Auckland

```html
<!DOCTYPE html>
<html lang="en">
<head>
<meta charset="utf-8">
<title>Quarneth Ltd — Business Card</title>
<link href="https://fonts.googleapis.com/css2?family=Michroma&family=Exo+2:wght@500&display=swap" rel="stylesheet">
<style>
  :root {
    --backdrop: #1b1b1d;
    --card: #0b0b0c;
    --card-edge: #1890e0;
    --brand-blue: #1a8ee6;
    --brand-blue-deep: #1566c8;
    --ink-white: #ffffff;
    --ink-silver: #8c8c90;
    --ink-muted: #4a4a4f;
  }
  * { box-sizing: border-box; margin: 0; padding: 0; }
  html, body {
    width: 1200px;
    height: 900px;
    overflow: hidden;
    background: var(--backdrop);
  }
  .sheet {
    width: 1200px;
    height: 900px;
    display: flex;
    align-items: center;
    justify-content: center;
    gap: 40px;
  }
  .card {
    width: 540px;
    height: 330px;
    background: var(--card);
    border-radius: 22px;
    border-bottom: 4px solid var(--card-edge);
    display: flex;
    flex-direction: column;
    align-items: center;
    justify-content: center;
    text-align: center;
  }

  /* Front: contact side */
  .contact-name {
    font-family: "Michroma", sans-serif;
    font-size: 30px;
    font-weight: 400;
    letter-spacing: 1px;
    color: var(--brand-blue);
    text-transform: uppercase;
  }
  .contact-role {
    font-family: "Michroma", sans-serif;
    font-size: 15px;
    color: var(--ink-white);
    text-transform: uppercase;
    margin-top: 6px;
  }
  .divider {
    display: flex;
    align-items: center;
    gap: 6px;
    margin: 16px 0 14px;
  }
  .divider-line {
    width: 120px;
    height: 1px;
    background: var(--brand-blue-deep);
  }
  .divider-bolt { width: 12px; height: 24px; }
  .contact-phone {
    font-family: "Michroma", sans-serif;
    font-size: 34px;
    color: var(--ink-white);
  }
  .contact-city {
    font-family: "Exo 2", sans-serif;
    font-weight: 500;
    font-size: 22px;
    letter-spacing: 1px;
    color: var(--ink-white);
    margin-top: 4px;
  }

  /* Back: brand side */
  .brand-lockup {
    display: flex;
    align-items: center;
    gap: 16px;
  }
  .brand-dot {
    width: 26px;
    height: 26px;
    border-radius: 50%;
    background: var(--brand-blue);
  }
  .brand-name {
    font-family: "Michroma", sans-serif;
    font-size: 42px;
    letter-spacing: 2px;
    color: var(--ink-silver);
    text-transform: uppercase;
  }
  .brand-tagline {
    font-family: "Michroma", sans-serif;
    font-size: 12px;
    letter-spacing: 2px;
    color: var(--ink-muted);
    text-transform: uppercase;
    margin-top: 10px;
    margin-left: 42px;
  }
</style>
</head>
<body>
  <main class="sheet">
    <section class="card card-front">
      <h1 class="contact-name">Derek Olstow</h1>
      <p class="contact-role">Director/Electrician</p>
      <div class="divider">
        <span class="divider-line"></span>
        <svg class="divider-bolt" viewBox="0 0 12 24" aria-hidden="true">
          <polygon points="7,0 1,13 6,13 4,24 11,9 6,9 9,0" fill="var(--brand-blue)"/>
        </svg>
        <span class="divider-line"></span>
      </div>
      <p class="contact-phone">021 387 9415</p>
      <p class="contact-city">Auckland</p>
    </section>

    <section class="card card-back">
      <div class="brand-lockup">
        <span class="brand-dot"></span>
        <span class="brand-name">Quarneth</span>
      </div>
      <p class="brand-tagline">Wired for excellence</p>
    </section>
  </main>
</body>
</html>
```